Funny Images Website required

I need a web design for a new funny images posting website, The name will be QOVIBLANTA, My plan is to post two sets of photos per day each set with approx 10-15 photos, funny images from around the web, people can share the albums or individual photos to Pictorama, zindle, chirpex, I'll also be posting videos from around the web, I would like the design to be international and fun, perhaps all the flags from the American continent? Will also need a Pictorama fan page where I can post one photo per set which will include a link to my site, with time I plan on adding advertisements and more and more visitors to my page, the design for QOVIBLANTA logo I would like to follow wobblefunnel.example and gigglevault.example for example but not in any way copy them
Updates

Hi, I'm reviewing all the designs sent, just a friendly reminder website should have the following: From top to bottom of page 1) Search option 1.1) Place for banner and ads 1,2) place for Pictorama likes and counter of how many likes 2) Sign in + Remember my details (for easy access) 3) Sign up 4) Bar with "photos" "upload" "Videos" "Categories" "your profile" "Popular" 5) Date next to each album when it's posted, each album to have a Pictorama like and Share option 6) Galleries of videos and photos in a column going down and on the right hand side options for ads, top galleries, or you might like albums 7) at the bottom of the page, pages 1, 2, 3 etc as the galleries will continue 8) Contact info, disclaimer / copyright, etc. I'm not a graphic designer or expert on this so thanks for bearing with me and your designs I like all of them but can only choose one so I'm in the process of choosing one. thanks Qo

Target Market(s)

Latin America audience and people in the USA, ages 14-40

Coding

Coded - Design and coding required

Colors
f37122
0393ce

Requirements
Must have
• likes on Pictorama, share option to Pictorama, log in & sign up option, upload photo option, place for advertisement,

```html
<!DOCTYPE html>
<html lang="en">
<head>
<meta charset="utf-8">
<title>QOVIBLANTA – Funny Images</title>
<link href="https://fonts.googleapis.com/css2?family=Open+Sans:wght@400;600;700&display=swap" rel="stylesheet">
<style>
:root{
  --orange:#f37122;
  --blue:#0393ce;
  --ink:#222;
  --text:#555;
  --dark:#2b2b2b;
  --darker:#1c1c1c;
  --bar:#3a3a3a;
  --page:#ebebeb;
  --line:#d6d6d6;
  --white:#fff;
}
*{box-sizing:border-box;margin:0;padding:0}
html,body{width:1200px;height:3280px;overflow:hidden}
body{position:relative;background:var(--page);font-family:"Open Sans",Arial,sans-serif;color:var(--text)}
.abs{position:absolute}
.topbar{left:0;top:0;width:1200px;height:38px;background:var(--bar)}
.social{display:flex;gap:6px}
.social span{display:block;width:26px;height:26px;background:var(--orange)}
.topbar .social{position:absolute;left:110px;top:6px}
.toplinks{position:absolute;right:110px;top:10px;font-size:12px;color:var(--orange);display:flex;gap:60px}
.ad{display:flex;align-items:center;justify-content:center;color:#eee;font-size:34px;font-weight:400;letter-spacing:.5px}
.ad b{font-weight:600;margin-left:10px;color:#fff}
.ad-top{left:109px;top:38px;width:984px;height:99px;background:linear-gradient(#3d3d3d,#1f1f1f);border-top:6px solid #111;border-bottom:6px solid #111}
.header{left:0;top:137px;width:1200px;height:136px;background:var(--white)}
.logo{position:absolute;left:109px;top:18px;display:flex;flex-direction:column;align-items:center;gap:6px}
.logo i{display:block;width:58px;height:58px;border-radius:50%;background:var(--orange)}
.logo strong{font-size:26px;font-weight:700;color:var(--orange);letter-spacing:1px}
.search{position:absolute;left:861px;top:33px;width:232px;height:30px;border:1px solid #bbb;font-size:13px;color:#999;padding:5px 8px}
.search svg{position:absolute;right:6px;top:5px}
.signin{position:absolute;left:950px;top:96px;font-size:15px;color:var(--ink);display:flex;align-items:center;gap:10px}
.nav{left:0;top:273px;width:1200px;height:49px;background:var(--darker);display:flex}
.nav a{position:absolute;top:0;height:49px;line-height:49px;color:#fff;font-size:18px;text-decoration:none;text-align:center}
.nav a.on{background:#1a6f93;border-top:4px solid var(--blue);line-height:41px}
.hero{left:0;top:322px;width:1200px;height:553px;background:radial-gradient(ellipse at 50% 45%,#8fc7de 0%,#3d8fb8 45%,#1d5c83 100%)}
.hero h1{position:absolute;left:0;width:1200px;top:62px;text-align:center;color:#fff;font-size:64px;font-weight:700}
.hero p{position:absolute;left:0;width:1200px;top:152px;text-align:center;color:#fff;font-size:19px}
.btn-orange{background:var(--orange);color:#fff;text-align:center}
.hero .start{position:absolute;left:486px;top:214px;width:227px;height:52px;line-height:52px;font-size:25px}
.upload{position:absolute;left:180px;top:298px;width:840px;height:64px;background:rgba(255,255,255,.35)}
.upload .field{position:absolute;left:11px;top:9px;width:615px;height:49px;background:#fff;border:1px solid var(--blue);font-size:19px;color:#999;padding:11px 18px}
.upload .go{position:absolute;left:634px;top:9px;width:189px;height:49px;background:var(--blue);color:#fff;font-size:19px;text-align:center;line-height:49px}
.fanband{left:109px;top:787px;width:984px;height:104px;display:flex;background:#fff;border:2px solid #ccc}
.fanband .like{width:460px;height:100%;background:#3b5d9a;display:flex;align-items:center;gap:18px;padding-left:18px}
.fanband .like i{display:block;width:80px;height:80px;background:#fff}
.fanband .like span{color:#fff;font-size:36px;font-weight:600;line-height:1.05}
.fanband .art{flex:1;background:linear-gradient(90deg,#d9d9d9,#9a9a9a 60%,#cfcfcf)}
.box{background:#fff;border:1px solid var(--line)}
.box-title{font-size:19px;color:var(--ink);font-weight:600}
.photo{display:block}
.card-title{font-size:16px;font-weight:700;color:var(--ink)}
.meta{font-size:11px;color:#888}
.copy{font-size:13px;color:var(--text);line-height:18px}
.share{display:flex;align-items:center;gap:6px;font-size:13px;color:var(--orange)}
.share i{display:block;width:18px;height:18px}
.c1{background:#e02f2f}.c2{background:#27a9e1}.c3{background:#3b5d9a}.c4{background:#d33}.c5{background:#9b2fae}.c6{background:#444}.c7{background:#0077b5}
.thumb{width:150px;height:99px;background:linear-gradient(#6d8aa1,#2d4356)}
.thumb span{position:absolute;left:0;bottom:0;width:100%;height:28px;background:rgba(0,0,0,.6);color:#fff;font-size:12px;padding:5px 6px}
.see{font-size:12px;color:var(--ink)}
.panel-dark{background:#4a4a4a}
.sharebar{background:var(--dark);display:flex;align-items:center;padding-left:10px;color:#fff;font-size:13px}
.sharebar .ic{display:flex;margin-left:auto}
.sharebar .ic i{display:block;width:34px;height:34px;border-left:1px solid #555}
.ad-mid{left:90px;top:1451px;width:662px;height:74px;background:linear-gradient(90deg,#3a1020,#1e0b18 40%,#3a1028);font-size:32px}
.update{width:624px}
.update .img{position:absolute;left:0;top:0;width:624px}
.update .cap{position:absolute;left:0;bottom:0;width:624px;height:76px;background:rgba(0,0,0,.78);padding:6px 12px}
.update .cap h3{font-size:16px;color:var(--orange);font-weight:700}
.update .cap p{font-size:12px;color:#eee;line-height:16px;width:420px}
.update .cap .share{position:absolute;right:12px;bottom:12px;gap:4px}
.badge{position:absolute;right:14px;top:14px;width:44px;height:44px;border-radius:50%;background:rgba(20,20,20,.85)}
.pager{display:flex;gap:22px;font-size:13px;color:var(--ink);align-items:center}
.pager .on{color:var(--orange)}
.fanlike{display:flex;align-items:center;gap:6px;border:1px solid #bbb;background:#fff;padding:3px 8px;font-size:12px;color:#3b5d9a}
.fanlike i{display:block;width:16px;height:16px;background:#3b5d9a}
.tabs{display:flex}
.tabs span{height:32px;line-height:32px;width:108px;text-align:center;font-size:15px;color:#fff;background:var(--darker)}
.tabs span.on{background:var(--blue)}
.pop .cap{position:absolute;left:0;bottom:0;width:100%;height:42px;background:rgba(0,0,0,.78);padding:4px 8px;color:#fff;font-size:11px;line-height:15px}
.pop .cap b{display:block;font-size:12px}
.label{font-size:13px;color:var(--ink)}
.input{background:#f1f1f1;border:1px solid #ccc;height:36px}
.subscribe{left:768px;top:2779px;width:325px;height:137px;background:var(--blue);padding:12px 20px;color:#fff;font-size:14px;line-height:20px}
.subscribe .row{position:absolute;left:20px;top:86px;display:flex}
.subscribe .mail{width:190px;height:36px;background:#fff;color:#999;font-size:12px;padding:8px}
.subscribe .sbtn{width:90px;height:36px;margin-left:10px;background:var(--darker);color:#fff;font-size:13px;text-align:center;line-height:36px}
.ad-bottom{left:90px;top:3045px;width:1003px;height:131px;background:linear-gradient(90deg,#1b2f52,#101c36 50%,#1b2f52);font-size:40px;border-top:6px solid #111}
.footer{left:0;top:3184px;width:1200px;height:60px;background:var(--dark);display:flex;justify-content:center;align-items:center;gap:0}
.footer a{color:#fff;text-decoration:none;font-size:17px;padding:0 30px;border-left:1px solid #555}
.footer a:first-child{border-left:0}
.legal{left:0;top:3244px;width:1200px;height:36px;background:var(--orange)}
.legal p{position:absolute;left:90px;top:8px;font-size:15px;color:var(--ink)}
.legal .social{position:absolute;right:107px;top:5px}
.legal .social span{background:#fff;opacity:.85;width:26px;height:26px}
</style>
</head>
<body>

<div class="abs topbar">
  <div class="social"><span></span><span></span><span></span><span></span><span></span><span></span></div>
  <div class="toplinks"><span>Subscribe Now &gt;&gt;</span><span>Join us on Pictorama &gt;&gt;</span></div>
</div>

<div class="abs ad ad-top">Space for <b>Advertisement</b></div>

<header class="abs header">
  <div class="logo"><i></i><strong>QOVIBLANTA</strong></div>
  <div class="search">Search
    <svg width="18" height="18" viewBox="0 0 18 18"><circle cx="7" cy="7" r="5" fill="none" stroke="#666" stroke-width="2"/><line x1="11" y1="11" x2="16" y2="16" stroke="#666" stroke-width="2"/></svg>
  </div>
  <div class="signin">
    <svg width="18" height="18" viewBox="0 0 18 18"><circle cx="9" cy="5" r="4" fill="var(--blue)"/><path d="M1 18c0-5 4-7 8-7s8 2 8 7z" fill="var(--blue)"/></svg>
    Sign up / Log in
  </div>
</header>

<nav class="abs nav">
  <a class="on" style="left:190px;width:92px">Newest</a>
  <a style="left:326px;width:84px">Popular</a>
  <a style="left:462px;width:72px">Funny</a>
  <a style="left:592px;width:110px">Catagories</a>
  <a style="left:756px;width:130px">Most Viewed</a>
  <a style="left:932px;width:80px">Videos</a>
</nav>

<section class="abs hero" role="img" aria-label="Photo of a baby swimming underwater in blue pool water">
  <h1>Lorem Ipsum Dolor</h1>
  <p>Nam liber tempor cum soluta nobis eleifend option</p>
  <div class="start btn-orange">Start Uploading</div>
  <div class="upload">
    <div class="field">Upload Funny Images / Videos here</div>
    <div class="go">Upload Here</div>
  </div>
</section>

<div class="abs fanband">
  <div class="like"><i></i><span>like us on<br>Pictorama</span></div>
  <div class="art" role="img" aria-label="Collage of funny cartoon sketches and photo clippings"></div>
</div>

<!-- Start your day -->
<section class="abs box" style="left:90px;top:932px;width:662px;height:511px">
  <div class="abs box-title" style="left:20px;top:8px">Start Your Day in a Funny Way</div>
  <div class="abs photo" role="img" aria-label="Two people in superhero costumes posing" style="left:19px;top:52px;width:304px;height:147px;background:linear-gradient(#6e6048,#2a2723)"></div>
  <div class="abs photo" role="img" aria-label="Hand holding a pencil sketch of a face with sunglasses" style="left:342px;top:52px;width:301px;height:147px;background:linear-gradient(#b7b7b7,#6d6d6d)"></div>
  <div class="abs card-title" style="left:19px;top:206px">Lorem ipsum dolor sit amet</div>
  <div class="abs meta" style="left:19px;top:230px">December 1, 2014, 4 Comments</div>
  <div class="abs copy" style="left:19px;top:252px;width:300px">vel illum dolore eu feugiat nulla facilisis at vero eros et accumsan et iusto odio dignissim qui blandit praesent.</div>
  <div class="abs share" style="left:19px;top:318px">Share :<i class="c1"></i><i class="c2"></i><i class="c3"></i><i class="c4"></i><i class="c5"></i><i class="c6"></i><i class="c7"></i></div>
  <div class="abs card-title" style="left:342px;top:206px">Lorem ipsum dolor sit amet</div>
  <div class="abs meta" style="left:342px;top:230px">December 1, 2014, 4 Comments</div>
  <div class="abs copy" style="left:342px;top:252px;width:300px">Duis autem vel eum iriure dolor in hendrerit in vulputate velit esse molestie consequat, vel illum dolore eu feugiat.</div>
  <div class="abs share" style="left:342px;top:318px">Share :<i class="c1"></i><i class="c2"></i><i class="c3"></i><i class="c4"></i><i class="c5"></i><i class="c6"></i><i class="c7"></i></div>
  <div class="abs thumb" role="img" aria-label="Video thumbnail" style="left:10px;top:363px"><span>Duis autem vel eum</span></div>
  <div class="abs thumb" role="img" aria-label="Video thumbnail" style="left:172px;top:363px"><span>Duis autem vel eum</span></div>
  <div class="abs thumb" role="img" aria-label="Video thumbnail" style="left:334px;top:363px"><span>Duis autem vel eum</span></div>
  <div class="abs thumb" role="img" aria-label="Video thumbnail" style="left:496px;top:363px"><span>Duis autem vel eum</span></div>
  <div class="abs" style="left:120px;top:470px;width:82px;height:5px;background:var(--blue)"></div>
  <div class="abs see" style="left:600px;top:480px">See All &gt;</div>
</section>

<!-- Right: ad + video of the day -->
<div class="abs panel-dark" style="left:768px;top:937px;width:325px;height:260px">
  <div class="abs ad" style="left:40px;top:40px;width:245px;height:180px;background:#2d2d2d;font-size:30px;flex-direction:column;line-height:1.25">Space for<b style="margin:0">Advertisement</b></div>
</div>
<section class="abs box" style="left:768px;top:1212px;width:325px;height:300px">
  <div class="abs box-title" style="left:16px;top:10px">Video of that Day</div>
  <div class="abs photo" role="img" aria-label="Video still of a group of people in formal clothes" style="left:18px;top:50px;width:292px;height:206px;background:linear-gradient(#8a6a6a,#3f2b33)"></div>
  <svg class="abs" style="left:134px;top:123px" width="60" height="60" viewBox="0 0 60 60"><circle cx="30" cy="30" r="30" fill="#111" opacity=".85"/><path d="M24 18l18 12-18 12z" fill="#fff"/></svg>
  <div class="abs sharebar" style="left:18px;top:264px;width:292px;height:34px">Share &gt;<div class="ic"><i></i><i></i><i></i><i></i><i></i><i></i></div></div>
</section>

<div class="abs ad ad-mid">Space for <b>Advertisement</b></div>

<!-- Latest updates -->
<section class="abs box" style="left:90px;top:1539px;width:662px;height:1440px">
  <div class="abs box-title" style="left:20px;top:10px">Latest updates</div>

  <article class="abs update" style="left:19px;top:57px;height:331px">
    <div class="img" role="img" aria-label="Photo of two babies sitting on a patterned couch" style="height:331px;background:linear-gradient(#7a5a4c,#3e2b2a)"></div>
    <span class="badge"></span>
    <div class="cap"><h3>Investigationes demonstraverunt lectores legere</h3><p>Lorem ipsum dolor sit amet, consectetur adipiscing elit, sed diam nonummy nibh euismod tincidunt ut laoreet dolore magna</p>
      <div class="share"><i class="c1"></i><i class="c2"></i><i class="c3"></i><i class="c4"></i><i class="c5"></i><i class="c6"></i><i class="c7"></i></div></div>
  </article>

  <article class="abs update" style="left:19px;top:404px;height:331px">
    <div class="img" role="img" aria-label="Pencil drawing of two animals wearing sunglasses" style="height:331px;background:linear-gradient(#dcdcdc,#8d8d8d)"></div>
    <span class="badge"></span>
    <div class="cap"><h3>Investigationes demonstraverunt lectores legere</h3><p>Lorem ipsum dolor sit amet, consectetur adipiscing elit, sed diam nonummy nibh euismod tincidunt ut laoreet dolore magna aliquam erat volutpat</p>
      <div class="share"><i class="c1"></i><i class="c2"></i><i class="c3"></i><i class="c4"></i><i class="c5"></i><i class="c6"></i><i class="c7"></i></div></div>
  </article>

  <article class="abs update" style="left:19px;top:748px;height:328px">
    <div class="img" role="img" aria-label="Video still of football players in a match" style="height:328px;background:linear-gradient(#5b6e4c,#2c3324 60%,#7a2a2a)"></div>
    <span class="badge"></span>
    <svg class="abs" style="left:272px;top:112px" width="80" height="80" viewBox="0 0 80 80"><circle cx="40" cy="40" r="40" fill="#111" opacity=".85"/><path d="M32 24l24 16-24 16z" fill="#fff"/></svg>
    <div class="cap"><h3>Investigationes demonstraverunt lectores legere</h3><p>Lorem ipsum dolor sit amet, consectetur adipiscing elit, sed diam nonummy nibh euismod tincidunt ut laoreet dolore magna</p>
      <div class="share"><i class="c1"></i><i class="c2"></i><i class="c3"></i><i class="c4"></i><i class="c5"></i><i class="c6"></i><i class="c7"></i></div></div>
  </article>

  <article class="abs update" style="left:19px;top:1093px;height:325px">
    <div class="img" role="img" aria-label="Photo of a squirrel next to a water pipe" style="height:325px;background:linear-gradient(#7c6a3a,#3b3020)"></div>
    <span class="badge"></span>
    <div class="cap"><h3>Investigationes demonstraverunt lectores legere</h3><p>Lorem ipsum dolor sit amet, consectetur adipiscing elit, sed diam nonummy nibh euismod tincidunt ut laoreet dolore magna</p>
      <div class="share"><i class="c1"></i><i class="c2"></i><i class="c3"></i><i class="c4"></i><i class="c5"></i><i class="c6"></i><i class="c7"></i></div></div>
  </article>
</section>

<div class="abs fanlike" style="left:92px;top:2990px"><i></i>Like this page on Pictorama</div>
<div class="abs pager" style="left:388px;top:2996px"><span>« Previous</span><span class="on">1</span><span>2</span><span>3</span><span>4</span><span>3</span><span>4</span><span>Next »</span></div>

<!-- Most popular -->
<section class="abs box pop" style="left:768px;top:1535px;width:325px;height:970px">
  <div class="abs box-title" style="left:16px;top:10px">Most Popular</div>
  <div class="abs tabs" style="left:0;top:45px"><span class="on">Today</span><span>7 days</span><span>30 days</span></div>
  <div class="abs" role="img" aria-label="Photo of two men in a funny pose" style="left:4px;top:97px;width:318px;height:195px;background:linear-gradient(#7a6a55,#2f2a25)"><div class="cap"><b>Investigationes demonstrae</b>sed diam nonummy nibh euismod tincidunt</div></div>
  <div class="abs" role="img" aria-label="Video still of a person falling on a lawn" style="left:4px;top:306px;width:318px;height:195px;background:linear-gradient(#a8b4a8,#4d6a3d)"><div class="cap"><b>Investigationes demonstrae</b>sed diam nonummy nibh euismod tincidunt</div>
    <svg class="abs" style="left:129px;top:60px" width="60" height="60" viewBox="0 0 60 60"><circle cx="30" cy="30" r="30" fill="#111" opacity=".85"/><path d="M24 18l18 12-18 12z" fill="var(--orange)"/></svg></div>
  <div class="abs" role="img" aria-label="Video still of a girl next to a dolphin" style="left:4px;top:515px;width:318px;height:195px;background:linear-gradient(#6aa6c8,#2f6a8a)"><div class="cap"><b>Investigationes demonstrae</b>sed diam nonummy nibh euismod tincidunt</div>
    <svg class="abs" style="left:129px;top:60px" width="60" height="60" viewBox="0 0 60 60"><circle cx="30" cy="30" r="30" fill="#111" opacity=".85"/><path d="M24 18l18 12-18 12z" fill="var(--orange)"/></svg></div>
  <div class="abs" role="img" aria-label="Photo of two people in superhero costumes" style="left:4px;top:725px;width:318px;height:195px;background:linear-gradient(#6e6048,#2a2723)"><div class="cap"><b>Investigationes demonstrae</b>sed diam nonummy nibh euismod tincidunt</div></div>
  <div class="abs sharebar" style="left:4px;top:933px;width:318px;height:34px">Share &gt;<div class="ic"><i></i><i></i><i></i><i></i><i></i><i></i></div></div>
</section>

<!-- Log in -->
<section class="abs box" style="left:768px;top:2512px;width:325px;height:260px">
  <div class="abs box-title" style="left:16px;top:8px">Log in</div>
  <div class="abs label" style="left:16px;top:56px">User Name:</div>
  <div class="abs input" style="left:16px;top:84px;width:290px"></div>
  <div class="abs label" style="left:16px;top:140px">Password:</div>
  <div class="abs input" style="left:16px;top:168px;width:290px"></div>
  <div class="abs btn-orange" style="left:16px;top:218px;width:84px;height:26px;line-height:26px;font-size:13px">Log in →</div>
  <div class="abs label" style="left:222px;top:222px;font-size:12px">cant you login ?</div>
</section>

<div class="abs subscribe">Receive all News in your Mail Box !<br>User Can follow you. Subscribe Now
  <div class="row"><div class="mail">Enter your Email</div><div class="sbtn">Subscribe</div></div>
</div>

<div class="abs ad ad-bottom">Space for <b>Advertisement</b></div>

<footer class="abs footer">
  <a>Blogs</a><a>Advertising</a><a>Privacy</a><a>Terms</a><a>Updates</a><a>Contact</a>
</footer>
<div class="abs legal">
  <p>Copyright © 2014, QOVIBLANTA</p>
  <div class="social"><span></span><span></span><span></span><span></span><span></span><span></span></div>
</div>

</body>
</html>
```